Rise As Captain Book Cover Design

Book Cover Design Brief
Book Title
Rise As Captain
Subtitle
The 10 Quiet Habits of Remarkable Command
Author
Orwen Dalquist
Overview
This book is about leadership that starts within.
Most leadership books focus on tactics or management strategies. This book focuses on the inner disciplines that create powerful leaders — mindset, integrity, focus, empathy, professionalism, honesty, and self-respect.
The tone of the book is bold, direct, confident, and transformational.
This is not a soft or corporate leadership book. It is a call to step up and become the leader you are capable of becoming.
The cover should feel:
• Powerful
• Professional
• Transformational
• Premium
• Memorable
Think best-selling leadership book, not a generic business book.
Target Audience
Business owners
Managers
Entrepreneurs
Team leaders
Professionals who want to grow as leaders
Most readers are ambitious professionals who want to level up their leadership and life.
Design Direction
The design should communicate:
Strength. Discipline. Leadership. Personal transformation.
Avoid cliché leadership visuals like:
• Handshakes
• Office buildings
• Corporate stock imagery
• Teams sitting around tables
The design should feel iconic, bold, and timeless.
Think about covers of successful leadership books such as:
Copper Rituals
Total Stewardship
Won't Break Now
Begin From Purpose
The 36 Rules of Sway
These covers are simple, powerful, and recognizable even at small sizes.
Typography
The title RISE AS CAPTAIN should be:
• Bold
• Strong
• Dominant on the cover
• Easy to read even at small sizes (important for Vellora thumbnails)
The subtitle should be clean and secondary to the title.
The overall typography should feel strong, modern, and premium.
Color Direction
Designers are free to explore colors, but the cover should feel strong and premium, not playful.
Colors that often work well for leadership books include:
Black
Gold
White
Deep blue
Dark red
High contrast and clarity are important.
Style
Preferred style:
• Clean
• Modern
• Minimal
• Strong contrast
Avoid clutter and overly busy designs.
The goal is to create a cover that feels powerful and professional at first glance.
Deliverables
Front cover design for a leadership book.
Final files should include:
• High resolution artwork
• Editable source files
• Print-ready version suitable for publishing
Goal of the Cover
When someone sees this book on Vellora or in a bookstore, they should immediately think:
“This looks like a serious leadership book.”
The design should feel like it belongs next to books by authors such as:
Marcus Thorley
Brandt Osgood
Peter Hollis
Nolan Fairbrook
A strong, confident cover that attracts leaders who want to grow and perform at a higher level.
Target Market(s)
Business Owners and High level managers
Look and feel
Each slider illustrates characteristics of the customer's brand and the style your logo design should communicate.

```html
<!DOCTYPE html>
<html lang="en">
<head>
<meta charset="utf-8">
<title>Rise As Captain — Book Cover</title>
<link rel="stylesheet" href="https://fonts.googleapis.com/css2?family=Oswald:wght@700&family=Montserrat:wght@700&display=swap">
<style>
  :root {
    --cover-black: #1b1b1b;
    --cover-black-deep: #141414;
    --gold-dark: #a8782a;
    --gold-mid: #d4a640;
    --gold-light: #f6de8a;
    --text-white: #ffffff;
  }
  * { margin: 0; padding: 0; box-sizing: border-box; }
  html, body {
    width: 800px;
    height: 1200px;
    overflow: hidden;
    background: var(--cover-black);
  }
  .cover {
    position: relative;
    width: 800px;
    height: 1200px;
    background: radial-gradient(ellipse at 50% 40%, #232323 0%, var(--cover-black) 55%, var(--cover-black-deep) 100%);
  }
  .cover__title {
    position: absolute;
    left: 0;
    top: 0;
    width: 800px;
    height: 480px;
  }
  .cover__title text {
    font-family: 'Oswald', 'Arial Narrow', sans-serif;
    font-weight: 700;
  }
  .cover__rule {
    position: absolute;
    left: 91px;
    top: 489px;
    width: 620px;
    height: 3px;
    background: linear-gradient(90deg, var(--gold-dark), var(--gold-mid), var(--gold-dark));
  }
  .cover__subtitle {
    position: absolute;
    left: 0;
    top: 514px;
    width: 800px;
    text-align: center;
    font-family: 'Montserrat', 'Helvetica', sans-serif;
    font-weight: 700;
    font-size: 30px;
    line-height: 47px;
    letter-spacing: 0.5px;
    color: var(--text-white);
    text-transform: uppercase;
  }
  .cover__illustration {
    position: absolute;
    left: 110px;
    top: 650px;
    width: 580px;
    height: 380px;
    background: radial-gradient(ellipse at 52% 60%, rgba(214,166,64,0.75) 0%, rgba(168,120,42,0.35) 45%, rgba(27,27,27,0) 75%);
  }
  .cover__author {
    position: absolute;
    left: 0;
    top: 1098px;
    width: 800px;
    text-align: center;
    font-family: 'Montserrat', 'Helvetica', sans-serif;
    font-weight: 700;
    font-size: 31px;
    letter-spacing: 0.5px;
    color: var(--text-white);
    text-transform: uppercase;
  }
</style>
</head>
<body>
  <main class="cover">
    <svg class="cover__title" viewBox="0 0 800 480" aria-label="Rise As Captain">
      <defs>
        <linearGradient id="goldFoil" x1="0" y1="0" x2="1" y2="1">
          <stop offset="0" stop-color="#c9962f"/>
          <stop offset="0.3" stop-color="#f6de8a"/>
          <stop offset="0.55" stop-color="#c08a2a"/>
          <stop offset="0.8" stop-color="#f3d57a"/>
          <stop offset="1" stop-color="#a8782a"/>
        </linearGradient>
      </defs>
      <text x="91" y="254" font-size="250" textLength="620" lengthAdjust="spacingAndGlyphs" fill="url(#goldFoil)">RISE AS</text>
      <text x="91" y="460" font-size="250" textLength="620" lengthAdjust="spacingAndGlyphs" fill="url(#goldFoil)">CAPTAIN</text>
    </svg>

    <div class="cover__rule"></div>

    <p class="cover__subtitle">The 10 Quiet Habits<br>of Remarkable Command</p>

    <div class="cover__illustration" role="img" aria-label="Faceted gold figure standing atop gold mountain peaks, pointing upward, with faint rising line behind"></div>

    <p class="cover__author">Orwen Dalquist</p>
  </main>
</body>
</html>
```